Terra Swift Business Card Design

We need to improve the design of our current business card. We are a erosion control, hydro seeding company that serves many markets. We are attaching the current business card and our logo as reference. You may also visit our site at www.terraswiftllc.example to reference.

```html
<!DOCTYPE html>
<html lang="en">
<head>
<meta charset="utf-8">
<title>Terra Swift Business Card</title>
<link rel="stylesheet" href="https://fonts.googleapis.com/css2?family=Roboto:wght@400;500;700&display=swap">
<style>
  :root {
    --bg: #d3d4d6;
    --paper: #ffffff;
    --green: #2ba56b;
    --green-dark: #3f6e57;
    --ink: #1e1e1e;
    --rule: #222222;
    --icon-tone: #5fc08f;
  }
  * { margin: 0; padding: 0; box-sizing: border-box; }
  html, body { width: 900px; height: 1200px; overflow: hidden; }
  body { background: var(--bg); font-family: "Roboto", Arial, sans-serif; position: relative; color: var(--ink); }

  .card { position: absolute; left: 135px; width: 630px; background: var(--paper); overflow: hidden; }
  .card-front { top: 215px; height: 357px; }
  .card-back { top: 628px; height: 359px; }

  .front-brand { height: 194px; display: flex; align-items: center; justify-content: center; gap: 14px; }
  .brand-name { color: var(--green-dark); font-weight: 700; font-size: 64px; letter-spacing: -1px; }
  .brand-dot { width: 22px; height: 22px; border-radius: 50%; background: var(--green); }
  .front-rule { height: 7px; background: var(--rule); }
  .markets { height: 156px; background: var(--green); display: flex; justify-content: space-between; padding: 18px 20px 0; }
  .market { width: 97px; display: flex; flex-direction: column; align-items: center; }
  .market-art { width: 66px; height: 66px; background: var(--icon-tone); border-radius: 4px; }
  .market-label { margin-top: 8px; color: #fff; font-weight: 700; font-size: 15px; line-height: 19px; text-align: center; white-space: nowrap; }

  .back-brand { position: absolute; left: 28px; top: 112px; width: 316px; display: flex; align-items: center; justify-content: center; gap: 10px; }
  .back-brand .brand-name { font-size: 42px; }
  .back-brand .brand-dot { width: 15px; height: 15px; }
  .divider { position: absolute; left: 367px; top: 47px; width: 2px; height: 189px; background: var(--rule); }
  .contact { position: absolute; left: 387px; top: 46px; font-size: 15px; line-height: 20px; }
  .person-name { color: var(--green); font-weight: 700; font-size: 21px; line-height: 26px; }
  .person-role { margin-bottom: 8px; }
  .address { margin-bottom: 8px; }
  .line { display: flex; align-items: center; gap: 6px; height: 23px; }
  .line svg { width: 13px; height: 13px; fill: var(--green); flex: none; }
  .gap { height: 6px; }
  .services { position: absolute; left: 0; right: 0; top: 260px; text-align: center; }
  .services-title { color: var(--green); font-weight: 500; font-size: 20px; margin-bottom: 8px; }
  .services-list { font-weight: 500; font-size: 15px; line-height: 21px; letter-spacing: 0.2px; }
  .sep { color: var(--green); font-weight: 700; margin: 0 4px; }
</style>
</head>
<body>
  <section class="card card-front">
    <div class="front-brand">
      <span class="brand-dot"></span>
      <span class="brand-name">Terra Swift</span>
    </div>
    <div class="front-rule"></div>
    <div class="markets">
      <div class="market"><div class="market-art" role="img" aria-label="Line icon of solar panels and sun"></div><div class="market-label">Utility-scale<br>Solar</div></div>
      <div class="market"><div class="market-art" role="img" aria-label="Line icon of a pickaxe and rock face"></div><div class="market-label">Mine<br>Sites</div></div>
      <div class="market"><div class="market-art" role="img" aria-label="Line icon of a gas pipe and valve"></div><div class="market-label">Natural<br>Gas</div></div>
      <div class="market"><div class="market-art" role="img" aria-label="Line icon of transmission towers"></div><div class="market-label">Transmission<br>Lines</div></div>
      <div class="market"><div class="market-art" role="img" aria-label="Line icon of a factory with chimneys"></div><div class="market-label">Industrial<br>Plants</div></div>
      <div class="market"><div class="market-art" role="img" aria-label="Line icon of a building under construction with crane"></div><div class="market-label">Private<br>Developments</div></div>
    </div>
  </section>

  <section class="card card-back">
    <div class="back-brand">
      <span class="brand-dot"></span>
      <span class="brand-name">Terra Swift</span>
    </div>
    <div class="divider"></div>
    <div class="contact">
      <div class="person-name">DALE WHITAKER</div>
      <div class="person-role">Chief Operating Officer</div>
      <div class="address">27 Larkspur Lane<br>Oak Harbor, NC 28000</div>
      <div class="line"><svg viewBox="0 0 16 16"><path d="M3 1l3 3-1.5 2c1 2 3 4 5 5L11.5 9.5l3 3-2 2.5C6 14 2 10 1 3z"/></svg>555-010-2468</div>
      <div class="line"><svg viewBox="0 0 16 16"><path d="M4 0h8v16H4zM5.5 2v10h5V2zM7 13.5h2v1H7z" fill-rule="evenodd"/></svg>555-010-7731</div>
      <div class="gap"></div>
      <div class="line"><svg viewBox="0 0 16 16"><path d="M1 3h14v10H1zM1 3l7 5 7-5"/></svg>dalew@terraswiftllc.example</div>
      <div class="line"><svg viewBox="0 0 16 16"><circle cx="8" cy="8" r="7"/></svg>www.terraswiftllc.example</div>
    </div>
    <div class="services">
      <div class="services-title">Services</div>
      <div class="services-list">
        Erosion Control<span class="sep">|</span>Seeding &amp; Mulching<span class="sep">|</span>Hydroseeding<span class="sep">|</span>Compost Blankets<br>
        Site Prep &amp; Grading<span class="sep">|</span>Laydown Construction &amp; Restoration<span class="sep">|</span>Filter Sock
      </div>
    </div>
  </section>
</body>
</html>
```